Fernhollow Ridge Farms
letterhead, envelope and business cards
Fernhollow Ridge Farms -
Creative Brief
Traditional
Tessa Harlan
3157 W Birch Mill Road North Platte, NE 68437
sales@fernhollowridgefarms.example
www.fernhollowridgefarms.example

```html
<!DOCTYPE html>
<html lang="en">
<head>
<meta charset="utf-8">
<title>Fernhollow Ridge Farms – Stationery</title>
<link href="https://fonts.googleapis.com/css2?family=Questrial&display=swap" rel="stylesheet">
<style>
  :root {
    --bg-outer: #4a4a4a;
    --bg-inner: #7a7a7a;
    --paper: #ffffff;
    --brown-dark: #5e3a1c;
    --brown: #7d5026;
    --brown-light: #a9743f;
    --faint: #e6ddd3;
    --card-back-1: #ffffff;
    --card-back-2: #d9d9d9;
    --window: #e4e4e4;
  }
  * { box-sizing: border-box; margin: 0; padding: 0; }
  html, body { width: 1200px; height: 737px; overflow: hidden; }
  body {
    font-family: "Questrial", "Century Gothic", sans-serif;
    background: radial-gradient(ellipse at center, var(--bg-inner) 0%, var(--bg-outer) 100%);
    position: relative;
  }
  .sheet { position: absolute; background: var(--paper); overflow: hidden; box-shadow: 0 2px 8px rgba(0,0,0,.35); }
  .band { position: absolute; left: 0; width: 100%; }
  .wordmark { position: absolute; color: var(--brown-dark); font-size: 30px; line-height: 1; white-space: nowrap; }
  .faint-art { position: absolute; background: linear-gradient(90deg, transparent, var(--faint) 20%, var(--faint) 80%, transparent); opacity: .8; border-radius: 40px 40px 0 0; }
  .white-text { color: #fff; position: absolute; white-space: nowrap; }

  /* Letterhead */
  .letterhead { left: 29px; top: 24px; width: 590px; height: 689px; }
  .letterhead .wordmark { left: 0; width: 100%; text-align: center; top: 50px; font-size: 34px; }
  .letterhead .footer-text { left: 0; width: 100%; text-align: center; bottom: 14px; font-size: 11px; line-height: 1.5; }

  /* Envelope */
  .envelope { left: 29px; top: 288px; width: 590px; height: 270px; }
  .envelope .wordmark { left: 26px; top: 30px; font-size: 24px; }
  .envelope .window { position: absolute; right: 26px; top: 78px; width: 242px; height: 70px; background: var(--window); border-radius: 4px; }
  .envelope .address { left: 10px; top: 200px; font-size: 13px; }

  /* Business card front */
  .card-front { left: 643px; top: 24px; width: 533px; height: 324px; }
  .card-front .contact { position: absolute; left: 22px; top: 12px; color: var(--brown-dark); font-size: 12px; line-height: 1.5; white-space: nowrap; }
  .card-front .name { right: 20px; top: 16px; font-size: 27px; }
  .card-front .wordmark { left: 24px; top: 142px; font-size: 21px; }
  .card-front .web { right: 18px; top: 160px; font-size: 13px; }
  .card-front .address { right: 20px; top: 262px; font-size: 13px; line-height: 1.6; text-align: right; }

  /* Business card back */
  .card-back { left: 643px; top: 379px; width: 533px; height: 324px; background: linear-gradient(180deg, var(--card-back-1) 30%, var(--card-back-2) 100%); }
  .card-back .wordmark { left: 0; width: 100%; text-align: center; top: 116px; font-size: 40px; }
  .card-back .web { position: absolute; left: 0; width: 100%; text-align: center; top: 252px; color: var(--brown); font-size: 20px; }
</style>
</head>
<body>

<section class="sheet letterhead">
  <div class="wordmark">Fernhollow Ridge Farms</div>
  <div class="faint-art" style="left:150px; top:540px; width:300px; height:60px;" role="img" aria-label="Faint farm animal silhouettes"></div>
  <svg class="band" style="bottom:0" width="590" height="110" viewBox="0 0 590 110" aria-hidden="true">
    <defs><linearGradient id="lhBrown" x1="0" x2="1"><stop offset="0" stop-color="#a9743f"/><stop offset=".5" stop-color="#7d5026"/><stop offset="1" stop-color="#5e3a1c"/></linearGradient></defs>
    <path d="M0 30 Q300 70 590 10 L590 110 L0 110 Z" fill="url(#lhBrown)"/>
  </svg>
  <div class="white-text footer-text">3157 W Birch Mill Road, North Platte, NE 68437 PH: 308-555-0142<br>E-mail: sales@fernhollowridgefarms.example www.fernhollowridgefarms.example</div>
</section>

<section class="sheet envelope">
  <div class="wordmark">Fernhollow Ridge Farms</div>
  <div class="window"></div>
  <div class="faint-art" style="left:60px; top:150px; width:260px; height:40px;" role="img" aria-label="Faint farm animal silhouettes"></div>
  <svg class="band" style="bottom:0" width="590" height="100" viewBox="0 0 590 100" aria-hidden="true">
    <defs><linearGradient id="envBrown" x1="0" x2="1"><stop offset="0" stop-color="#7d5026"/><stop offset=".6" stop-color="#a9743f"/><stop offset="1" stop-color="#7d5026"/></linearGradient></defs>
    <path d="M0 20 L330 20 Q460 22 590 0 L590 100 L0 100 Z" fill="url(#envBrown)"/>
  </svg>
  <div class="white-text address">3157 W Birch Mill Road, North Platte, NE 68437</div>
</section>

<section class="sheet card-front">
  <svg class="band" style="top:0" width="533" height="324" viewBox="0 0 533 324" aria-hidden="true">
    <defs><linearGradient id="cardBrown" x1="0" x2="1"><stop offset="0" stop-color="#a9743f"/><stop offset=".5" stop-color="#7d5026"/><stop offset="1" stop-color="#5e3a1c"/></linearGradient></defs>
    <path d="M300 0 L533 0 L533 324 L250 324 Q260 160 300 0 Z" fill="url(#cardBrown)"/>
  </svg>
  <div class="contact">PH: 308-555-0142<br>E-mail: sales@fernhollowridgefarms.example</div>
  <div class="white-text name">Tessa Harlan</div>
  <div class="wordmark">Fernhollow Ridge Farms</div>
  <div class="faint-art" style="left:20px; top:255px; width:220px; height:50px;" role="img" aria-label="Faint farm animal silhouettes"></div>
  <div class="white-text web">www.fernhollowridgefarms.example</div>
  <div class="white-text address">3157 W Birch Mill Road<br>North Platte, NE 68437</div>
</section>

<section class="sheet card-back">
  <div class="wordmark">Fernhollow Ridge Farms</div>
  <div class="web">www.fernhollowridgefarms.example</div>
</section>

</body>
</html>
```